Business card design for new eCommerce site focusing on integrity and strong businsess tactics

We need a business card that will stand out and be memorable. Something with color that matches our company logo colors. Think high end version of Tallyhop. There are 2 logos provided. The parent company is called Brightwell Craft Partners and we are presenting a new and very exciting eCommerce site called KestrelTradeHub.example.

Target Market(s)

Our target markets are in the Activities, Food and Beverage, Health and Beauty

Industry/Entity Type

Marketing

Contact Information for Business Card

We have 4 members that need cards...I will provide all info to the winner of the design contest
Business Address is
47390 West 63rd Lane, Suite K204
Phoenix AZ 85061

Font styles to use
Serif
Sans Serif

Colors

Designer to choose colors to be used in the design.

Requirements
Must have
• The card must be memorable...should be unique in design but must exude integrity and be playful .
• I have provided several colors or our parent company...please feel free to use which ever
Nice to have
• I will leave this up to you. Feel free to use other images of your choosing that wraps around our client.....Activities, Dining, Health, Beauty
Should not have
• just dont be boring

```html
<!DOCTYPE html>
<html lang="en">
<head>
<meta charset="utf-8">
<title>Brightwell Craft Partners — Business Card</title>
<link rel="stylesheet" href="https://fonts.googleapis.com/css2?family=Montserrat:wght@600&family=Open+Sans:wght@400;600&display=swap">
<style>
  :root {
    --backdrop: #d7d7d7;
    --paper: #ffffff;
    --brand-teal: #2b9a8e;
    --brand-blue: #2a73ad;
    --name-blue: #2f6fae;
    --accent-green: #7cc242;
    --ink-grey: #6f6f6f;
    --soft-grey: #8c8c8c;
  }
  * { box-sizing: border-box; margin: 0; padding: 0; }
  html, body { width: 1200px; height: 800px; overflow: hidden; }
  body {
    background: var(--backdrop);
    font-family: "Open Sans", Arial, sans-serif;
    position: relative;
  }
  .card {
    position: absolute;
    left: 290px;
    width: 620px;
    height: 354px;
    box-shadow: 0 4px 14px rgba(0,0,0,0.18);
    overflow: hidden;
  }
  .card--front { top: 30px; background: var(--paper); }
  .card--back {
    top: 416px;
    background: var(--brand-blue);
    display: flex;
    align-items: center;
    justify-content: center;
    gap: 16px;
  }
  .wordmark {
    position: absolute;
    left: 34px;
    top: 52px;
    display: flex;
    align-items: center;
    gap: 12px;
  }
  .wordmark__dot {
    width: 22px; height: 22px; border-radius: 50%;
    background: var(--brand-teal);
  }
  .wordmark__name {
    font-family: "Montserrat", Arial, sans-serif;
    font-weight: 600;
    font-size: 28px;
    color: var(--brand-teal);
    letter-spacing: 0.2px;
  }
  .person {
    position: absolute;
    left: 34px;
    top: 150px;
  }
  .person__name {
    font-weight: 600;
    font-size: 19px;
    color: var(--name-blue);
    line-height: 1.2;
  }
  .person__role {
    font-size: 16px;
    color: var(--ink-grey);
    line-height: 1.25;
  }
  .divider {
    position: absolute;
    left: 34px;
    right: 30px;
    top: 206px;
    height: 1px;
    background: var(--accent-green);
  }
  .partner {
    position: absolute;
    right: 30px;
    top: 150px;
    text-align: right;
  }
  .partner__name {
    font-size: 19px;
    font-weight: 600;
    color: var(--accent-green);
    line-height: 1.2;
  }
  .partner__tagline {
    font-size: 10px;
    color: var(--ink-grey);
    letter-spacing: 0.3px;
  }
  .contacts {
    position: absolute;
    left: 34px;
    top: 222px;
    list-style: none;
  }
  .contacts__item {
    display: flex;
    align-items: center;
    gap: 10px;
    font-size: 13px;
    color: var(--soft-grey);
    line-height: 22px;
  }
  .contacts__icon { width: 12px; height: 12px; flex: none; }
  .address {
    position: absolute;
    right: 30px;
    top: 226px;
    text-align: right;
    font-size: 13px;
    color: var(--soft-grey);
    line-height: 20px;
    font-style: normal;
  }
  .edge-band {
    position: absolute;
    left: 0; right: 0; bottom: 0;
    height: 8px;
    display: flex;
  }
  .edge-band__green { flex: 0 0 66%; background: var(--accent-green); }
  .edge-band__blue { flex: 1; background: var(--brand-blue); }
  .back__dot {
    width: 30px; height: 30px; border-radius: 50%;
    background: #ffffff;
  }
  .back__name {
    font-family: "Montserrat", Arial, sans-serif;
    font-weight: 600;
    font-size: 30px;
    color: #ffffff;
  }
</style>
</head>
<body>

<section class="card card--front" aria-label="Business card front">
  <div class="wordmark">
    <span class="wordmark__dot"></span>
    <span class="wordmark__name">Brightwell Craft Partners</span>
  </div>

  <div class="person">
    <p class="person__name">Darren Halloway</p>
    <p class="person__role">Founder</p>
  </div>

  <div class="partner">
    <p class="partner__name">KestrelTradeHub.example</p>
    <p class="partner__tagline">Activities-Dining-Health-Beauty</p>
  </div>

  <div class="divider"></div>

  <ul class="contacts">
    <li class="contacts__item">
      <svg class="contacts__icon" viewBox="0 0 12 12" aria-hidden="true"><rect x="3" y="0.5" width="6" height="11" rx="1" fill="none" stroke="#2f6fae" stroke-width="1.2"/><circle cx="6" cy="9.6" r="0.7" fill="#2f6fae"/></svg>
      0417 552 390
    </li>
    <li class="contacts__item">
      <svg class="contacts__icon" viewBox="0 0 12 12" aria-hidden="true"><rect x="0.5" y="2" width="11" height="8" fill="#2f6fae"/><path d="M0.5 2 L6 6.5 L11.5 2" fill="none" stroke="#fff" stroke-width="1"/></svg>
      info@kestreltradehub.example
    </li>
    <li class="contacts__item">
      <svg class="contacts__icon" viewBox="0 0 12 12" aria-hidden="true"><circle cx="5" cy="5" r="3.6" fill="none" stroke="#2f6fae" stroke-width="1.5"/><path d="M7.6 7.6 L11 11" stroke="#2f6fae" stroke-width="1.8" stroke-linecap="round"/></svg>
      www.kestreltradehub.example
    </li>
  </ul>

  <address class="address">
    47390 West 63rd Lane,<br>
    Suite K204 Phoenix AZ 85061
  </address>

  <div class="edge-band">
    <span class="edge-band__green"></span>
    <span class="edge-band__blue"></span>
  </div>
</section>

<section class="card card--back" aria-label="Business card back">
  <span class="back__dot"></span>
  <span class="back__name">Brightwell Craft Partners</span>
</section>

</body>
</html>
```